Business Card Designs

Looking to design a 3.5" x 2" standard business card for our employees.
The design needs to be sleek, simple, and modern. We would like our logo (attached) to be incorporated, but not in that colour, rather an outline of the logo in either gold or silver (whichever looks better).

Modern and Simple is what we are looking for, but be creative in incorporating the logo.

```html
<!DOCTYPE html>
<html lang="en">
<head>
<meta charset="UTF-8">
<title>Harbourline Suites – Business Card</title>
<link rel="stylesheet" href="https://fonts.googleapis.com/css2?family=Montserrat:wght@400;500;700&display=swap">
<style>
  :root {
    --teal: #62a3a1;
    --white: #ffffff;
    --ink: #1d1d1d;
    --backdrop: #e6e6e4;
    --card-shadow: 0 14px 30px rgba(0, 0, 0, 0.18);
  }
  * { box-sizing: border-box; margin: 0; padding: 0; }
  html, body {
    width: 1200px;
    height: 900px;
    overflow: hidden;
    background: var(--backdrop);
    font-family: "Montserrat", sans-serif;
  }
  .canvas { position: relative; width: 1200px; height: 900px; }

  .card {
    position: absolute;
    width: 560px;
    height: 320px;
    box-shadow: var(--card-shadow);
  }

  /* Front side */
  .card-front {
    left: 90px;
    top: 120px;
    background: var(--teal);
    display: flex;
    align-items: center;
    justify-content: center;
  }
  .brand {
    display: flex;
    align-items: center;
    gap: 14px;
    font-weight: 500;
    letter-spacing: 0.22em;
    text-transform: uppercase;
  }
  .brand-square { display: block; }
  .card-front .brand { color: var(--white); font-size: 22px; }
  .card-front .brand-square { width: 22px; height: 22px; background: var(--white); }

  /* Back side */
  .card-back {
    left: 550px;
    top: 460px;
    background: var(--white);
    color: var(--ink);
  }
  .back-brand {
    position: absolute;
    left: 34px;
    top: 104px;
    width: 190px;
  }
  .card-back .brand {
    color: var(--teal);
    font-size: 13px;
    letter-spacing: 0.16em;
    gap: 10px;
  }
  .card-back .brand-square { width: 14px; height: 14px; background: var(--teal); flex: none; }

  .divider {
    position: absolute;
    left: 244px;
    top: 48px;
    width: 1.5px;
    height: 150px;
    background: var(--teal);
  }

  .details { position: absolute; left: 272px; top: 40px; }
  .person-name {
    color: var(--teal);
    font-weight: 700;
    font-size: 20px;
    letter-spacing: 0.02em;
    text-transform: uppercase;
    line-height: 1.1;
  }
  .person-role { font-size: 13px; margin-top: 3px; }
  .contact-list { list-style: none; margin-top: 22px; }
  .contact-item {
    display: flex;
    align-items: center;
    gap: 10px;
    font-size: 13px;
    line-height: 1;
    margin-bottom: 9px;
  }
  .contact-icon { width: 15px; height: 15px; flex: none; fill: var(--teal); }

  .address {
    position: absolute;
    left: 34px;
    right: 30px;
    bottom: 58px;
    font-size: 16px;
    font-weight: 500;
    text-align: center;
  }
</style>
</head>
<body>
<main class="canvas">
  <section class="card card-front" aria-label="Business card front">
    <div class="brand"><span class="brand-square"></span>Harbourline Suites</div>
  </section>

  <section class="card card-back" aria-label="Business card back">
    <div class="back-brand">
      <div class="brand"><span class="brand-square"></span>Harbourline Suites</div>
    </div>
    <div class="divider"></div>
    <div class="details">
      <h1 class="person-name">Dalen Whitcombe</h1>
      <p class="person-role">Managing Director</p>
      <ul class="contact-list">
        <li class="contact-item">
          <svg class="contact-icon" viewBox="0 0 16 16" aria-hidden="true">
            <path d="M2 5c0-1.5 2-2.5 6-2.5S14 3.5 14 5v1.2h-3V5.2c-1-.4-5-.4-6 0v1H2z"/>
            <path d="M4.5 7h7l2 6.5h-11z"/>
          </svg>
          555-014-2873
        </li>
        <li class="contact-item">
          <svg class="contact-icon" viewBox="0 0 16 16" aria-hidden="true">
            <path d="M1 3.5h14v9H1z M2.3 4.5 8 9l5.7-4.5z" fill-rule="evenodd"/>
          </svg>
          hello@harbourlinesuites.com
        </li>
        <li class="contact-item">
          <svg class="contact-icon" viewBox="0 0 16 16" aria-hidden="true">
            <circle cx="8" cy="8" r="7"/>
            <path d="M4 5.5c1-.6 2.2-.2 2.6.6.4.9-.4 1.6.3 2.5.6.8-.2 1.8-1 2.3-.5-.9-1.2-1.3-1.6-2.3C3.9 7.7 3.4 6.4 4 5.5zM9.5 3.5c1.2.1 2.6.9 3.2 2-.8.3-1.7 0-2.2.6-.5.6-1.4.3-1.5-.5-.2-.8.9-1.1.5-2.1z" fill="var(--white)"/>
          </svg>
          www.harbourlinesuites.com
        </li>
      </ul>
    </div>
    <p class="address">418 Laurier Crescent Ottawa, ON, K1P 4R7</p>
  </section>
</main>
</body>
</html>
```